you will use Ai to Copy the website Quellabyx.com to come up with the basic frame work and it will give you the understanding of how I would like Zandoprik.com to be like. Zandoprik.com is a peer to peer rv rental site very similar to both of the other rv rental sites the difference is that are commission based 20% and above per rental and we will be one flat monthly rate and they keep all the earnings. Below is photo that will help you with the color scheme and the look and feel of the design

```html
<!DOCTYPE html>
<html lang="en">
<head>
<meta charset="utf-8">
<title>Zandoprik.com – RV Rentals</title>
<link href="https://fonts.googleapis.com/css2?family=Fira+Sans+Condensed:wght@500;600;700&family=Montserrat:wght@400;500;600;700&display=swap" rel="stylesheet">
<style>
:root{
  --green:#4f8a25;
  --green-dark:#3d6f1b;
  --lime:#a6c83a;
  --ink:#1d2127;
  --navy:#141a2e;
  --muted:#6c7077;
  --paper:#edeee8;
  --sage:#dfe6d3;
  --footer:#2f4636;
  --white:#fff;
  --line:#e2e3de;
}
*{box-sizing:border-box;margin:0;padding:0}
html,body{width:1200px;height:4882px;overflow:hidden}
body{position:relative;background:var(--white);font-family:"Montserrat",sans-serif;color:var(--ink)}
.abs{position:absolute}
.head-font{font-family:"Fira Sans Condensed",sans-serif}
.photo{display:block;overflow:hidden}
.btn{display:inline-flex;align-items:center;justify-content:center;background:var(--green);color:#fff;font-weight:600;border-radius:40px;font-size:14px}

/* header */
.site-header{left:0;top:0;width:1200px;height:80px;z-index:5}
.brand{left:63px;top:26px;font-weight:700;font-size:20px;color:var(--ink)}
.main-nav{left:500px;top:30px;display:flex;gap:26px;font-size:14px;font-weight:500}
.main-nav .active{border-bottom:2px solid var(--ink);padding-bottom:5px}
.header-actions{left:950px;top:24px;display:flex;gap:10px;align-items:center}
.host-btn{background:var(--navy);color:#fff;font-size:11px;font-weight:600;padding:8px 18px;border-radius:20px}
.icon-circle{width:30px;height:30px;border:1.5px solid var(--ink);border-radius:50%;display:flex;align-items:center;justify-content:center}

/* hero */
.hero{left:0;top:0;width:1200px;height:720px;background:linear-gradient(180deg,#e8eef1 0%,#c8d5dc 22%,#8ea4b1 40%,#6e8c9e 52%,#70895a 64%,#5f7e3c 80%,#6d8d42 100%)}
.hero-title{left:0;top:172px;width:1200px;text-align:center;font-family:"Fira Sans Condensed",sans-serif;font-weight:700;font-size:62px;line-height:1.14;color:var(--ink)}
.hero-title span{color:var(--green)}
.hero-badge{left:470px;top:328px;width:252px;height:252px;border-radius:50%;background:radial-gradient(circle at 50% 40%,#e8a24b 0%,#7a4c52 45%,#1d2a3b 80%);border:8px solid #6f9a30;box-shadow:0 0 0 4px rgba(255,255,255,.35)}
.hero-badge-name{left:470px;top:472px;width:252px;text-align:center;color:#fff;font-weight:700;font-size:26px}
.lime-band{top:716px;height:18px;background:var(--lime)}
.search-bar{left:114px;top:671px;width:972px;height:88px;background:#fff;border-radius:44px;box-shadow:0 6px 24px rgba(0,0,0,.12);display:flex;align-items:center;padding:0 0 0 32px}
.search-field{height:60px;padding:10px 16px;border-right:1px solid var(--line);display:flex;flex-direction:column;justify-content:center}
.search-field label{font-size:11px;color:var(--muted);margin-bottom:6px}
.search-field b{font-size:15px;font-weight:600}
.search-go{width:68px;height:68px;border-radius:50%;background:var(--navy);margin-left:auto;margin-right:10px;display:flex;align-items:center;justify-content:center}

/* promo */
.promo{top:800px;width:316px;height:180px;border-radius:4px;overflow:hidden}
.promo-text{left:20px;top:88px;color:#fff;font-family:Georgia,serif;font-size:17px;line-height:1.3}
.promo-btn{left:20px;top:142px;background:#fff;color:var(--ink);font-size:9px;font-weight:600;padding:5px 12px;border-radius:10px}

/* mission */
.mission-bg{left:0;top:985px;width:1200px;height:465px;background:var(--paper)}
.mission-title{left:686px;top:1066px;font-size:34px;font-weight:700}
.mission-text{left:686px;top:1118px;width:430px;font-size:13.5px;line-height:1.55;color:#4a4e55}
.mission-text p+p{margin-top:14px}
.clients{left:366px;top:1332px;width:278px;height:70px;background:#fff;border-radius:35px;display:flex;align-items:center;padding-left:18px;gap:14px}
.smile{width:44px;height:44px;border-radius:50%;background:#f7c624}
.clients b{display:block;font-size:20px;font-family:"Fira Sans Condensed",sans-serif}
.clients span{font-size:17px;font-family:"Fira Sans Condensed",sans-serif}

/* section titles */
.section-title{left:0;width:1200px;text-align:center;font-family:"Fira Sans Condensed",sans-serif;font-weight:700;font-size:34px;line-height:1.2}
.section-sub{left:0;width:1200px;text-align:center;font-size:14px;color:var(--muted)}

.tabs{left:404px;top:1640px;display:flex;gap:14px}
.tab{font-size:10px;padding:7px 14px;border:1px solid var(--line);border-radius:16px;color:var(--muted);display:flex;gap:6px;align-items:center}
.tab.active{background:var(--green);border-color:var(--green);color:#fff}
.tab i{width:10px;height:8px;border:1px solid currentColor;border-radius:2px}

/* rental card */
.rental{width:299px;height:352px;background:#fff;border-radius:8px;box-shadow:0 2px 10px rgba(0,0,0,.08);overflow:hidden}
.rental .photo{width:299px;height:224px}
.rental .deal{left:14px;top:12px;background:var(--lime);color:#fff;font-size:8px;font-weight:700;padding:3px 9px;border-radius:8px}
.rental .fav{left:266px;top:10px;width:22px;height:22px;border-radius:50%;background:#fff;display:flex;align-items:center;justify-content:center}
.dots{display:flex;gap:4px}
.dots i{width:6px;height:2px;background:rgba(255,255,255,.6);border-radius:2px}
.dots i.on{width:14px;background:#fff}
.rental .dots{left:124px;top:212px}
.rental h3{left:14px;top:238px;font-size:13px;font-weight:600}
.rental .loc{left:14px;top:262px;font-size:9px;color:var(--muted)}
.rental .tags{left:14px;top:282px;display:flex;gap:6px}
.rental .tags span{font-size:8px;color:var(--muted);background:#eeefec;padding:3px 14px;border-radius:8px}
.rental .price{left:14px;top:312px;font-size:19px;font-weight:700}
.rental .price small{font-size:9px;font-weight:400;color:var(--muted)}
.rental .rate{left:236px;top:318px;font-size:9px;color:var(--muted)}
.rental .rate i{color:#f2b01e;font-style:normal}

/* destinations */
.dest{top:2613px;width:186px;height:82px;background:#f1f1ee;display:flex;align-items:center;gap:12px;padding-left:26px}
.dest b{display:block;font-size:17px;font-family:"Fira Sans Condensed",sans-serif}
.dest span{font-size:12px;color:var(--muted)}
.arrow-btn{width:26px;height:26px;border-radius:50%;background:#fff;border:1px solid var(--line);display:flex;align-items:center;justify-content:center}

/* feature */
.feature-panel{left:760px;top:2736px;width:377px;height:501px;background:var(--sage);border-radius:16px;padding:22px 20px}
.feature-icon{width:60px;height:60px;border-radius:50%;background:var(--green);margin-bottom:18px}
.feature-panel p{font-size:11px;line-height:1.5;color:#4a4e55;margin-bottom:10px}
.perk{display:flex;gap:10px;margin-top:10px}
.perk svg{flex:none;margin-top:1px}
.perk b{font-size:11.5px;display:block}
.perk span{font-size:9.5px;color:var(--muted);line-height:1.4}

/* parks */
.parks-bg{left:0;top:3270px;width:1200px;height:600px;background:var(--paper)}
.park{top:3415px;width:343px;height:402px;border-radius:4px;overflow:hidden}
.park h3{left:18px;top:252px;color:#fff;font-family:"Fira Sans Condensed",sans-serif;font-size:27px;font-weight:700}
.park .region{left:18px;top:288px;color:#fff;font-size:13px}
.park .book{left:18px;top:314px;background:#9ebe3b;color:#fff;font-size:12px;padding:9px 18px;border-radius:18px}
.park .fav{left:303px;top:12px;width:30px;height:30px;border-radius:50%;background:#fff;display:flex;align-items:center;justify-content:center}
.park .dots{left:152px;top:380px}

/* news */
.news{top:3976px;width:343px;height:432px;background:#f1f1ee}
.news .photo{width:343px;height:265px}
.news .tag{left:12px;top:12px;background:#fff;font-size:10px;font-weight:600;padding:4px 10px;border-radius:4px}
.news h3{left:16px;top:282px;width:310px;font-size:15px;line-height:1.3;font-family:"Fira Sans Condensed",sans-serif;font-weight:700}
.news .excerpt{left:16px;top:328px;width:310px;font-size:10px;line-height:1.45;color:var(--muted)}
.news .more{left:16px;top:402px;font-size:10px;font-weight:700;text-decoration:underline}

/* footer */
.site-footer{left:0;top:4525px;width:1200px;height:341px;background:var(--footer);color:#fff}
.footer-brand{left:66px;top:118px;font-size:30px;font-weight:700}
.socials{left:90px;top:180px;display:flex;gap:14px}
.socials i{width:16px;height:16px;border:2px solid #fff;border-radius:50%}
.footer-col{top:68px}
.footer-col h4{font-family:"Fira Sans Condensed",sans-serif;font-size:19px;font-weight:700;margin-bottom:16px}
.footer-col li{list-style:none;font-size:10px;line-height:24px;opacity:.9}
.legal{left:0;top:4866px;width:1200px;height:16px;background:#f4f4f1;font-size:8px;color:var(--muted);display:flex;justify-content:space-between;padding:3px 63px}
</style>
</head>
<body>

<!-- Hero -->
<div class="abs hero photo" role="img" aria-label="Mountain lake landscape with a winding road through green hills"></div>
<header class="abs site-header">
  <div class="abs brand">Zandoprik.com</div>
  <nav class="abs main-nav"><span class="active">RV Rentals</span><span>Campgrounds</span></nav>
  <div class="abs header-actions">
    <span class="host-btn">Become a host</span>
    <span class="icon-circle"><svg width="14" height="14" viewBox="0 0 14 14" fill="none" stroke="#1d2127" stroke-width="1.4"><circle cx="7" cy="5" r="2.6"/><path d="M2 13c1-3 9-3 10 0"/></svg></span>
    <span class="icon-circle"><svg width="14" height="12" viewBox="0 0 14 12" stroke="#1d2127" stroke-width="1.4"><path d="M2 2h10M2 6h10M2 10h10"/></svg></span>
  </div>
</header>
<h1 class="abs hero-title">Start your adventure<br>with <span>an RV rental</span></h1>
<div class="abs hero-badge photo" role="img" aria-label="Round badge showing a motorhome parked at sunset"></div>
<div class="abs hero-badge-name">Zandoprik.com</div>
<div class="abs lime-band" style="left:21px;width:94px"></div>
<div class="abs lime-band" style="left:1085px;width:94px"></div>

<form class="abs search-bar">
  <div class="search-field" style="width:248px;position:relative"><label>Location</label><b>Milan, 25</b>
    <svg style="position:absolute;right:14px;top:26px" width="12" height="12" stroke="#999" stroke-width="1.4"><path d="M1 1l10 10M11 1L1 11"/></svg></div>
  <div class="search-field" style="width:182px"><label>Dates</label><b>Sep 24 - Oct 5</b></div>
  <div class="search-field" style="width:137px"><label>Guests</label><b>2 guests</b></div>
  <div class="search-field" style="width:137px"><label>Driver's age</label><b>25+</b></div>
  <div class="search-field" style="width:130px;border:none"><label>Rental type</label><b>All types &#8964;</b></div>
  <div class="search-go"><svg width="26" height="26" viewBox="0 0 26 26" fill="none" stroke="#fff" stroke-width="2.4"><circle cx="11" cy="11" r="7"/><path d="M16 16l6 6"/></svg></div>
</form>

<!-- Promo cards -->
<div class="abs promo photo" style="left:112px;background:linear-gradient(160deg,#8b9a84,#3e4a3a 60%,#27301f)" role="img" aria-label="Travel trailer set up at a forest campsite">
  <div class="abs promo-text">Less set up.<br>More quality time.</div><span class="abs promo-btn">Get it delivered</span></div>
<div class="abs promo photo" style="left:442px;background:linear-gradient(160deg,#6b6258,#3f3a36 60%,#2a2724)" role="img" aria-label="Motorhome driving on a hillside road">
  <div class="abs promo-text">Pick it up &amp;<br>hit the road</div><span class="abs promo-btn">Pick it up</span></div>
<div class="abs promo photo" style="left:773px;background:linear-gradient(180deg,#b9ccd8,#7a98a8 55%,#4c5a4a)" role="img" aria-label="Pickup truck towing a travel trailer on a highway">
  <div class="abs promo-text">Travel with<br>the trailer</div><span class="abs promo-btn">Pick it up</span></div>

<!-- Mission -->
<div class="abs mission-bg"></div>
<div class="abs photo" style="left:63px;top:1048px;width:280px;height:354px;border-radius:0 0 0 120px;background:linear-gradient(180deg,#7b8fa8 0%,#e7a86a 48%,#3e3b3c 70%,#222 100%)" role="img" aria-label="Camper van parked on a gravel lot at dusk"></div>
<div class="abs photo" style="left:366px;top:1010px;width:278px;height:294px;border-radius:0 60px 0 0;background:linear-gradient(180deg,#d9cdb8,#b99a74 50%,#6a5a48)" role="img" aria-label="Friends relaxing in camp chairs beside an RV"></div>
<div class="abs clients"><span class="smile"></span><div><b>500K+</b><span>Satisfied Clients</span></div></div>
<h2 class="abs mission-title head-font">Our mission</h2>
<div class="abs mission-text">
  <p>Restore people's relationship with the outdoors and each other by solving foundational human problems and creating lasting memories through exceptional outdoor experiences.</p>
  <p>The Quellabyx Group is a travel and hospitality company that integrates marketplace technology, insurance, and real estate to create unforgettable outdoor experiences.</p>
</div>
<span class="abs btn" style="left:686px;top:1298px;width:194px;height:40px">Letter from our CEO</span>

<!-- Rentals -->
<h2 class="abs section-title" style="top:1500px">Find the best RV rentals<br>in the country</h2>
<p class="abs section-sub" style="top:1593px">Explore the open road in the perfect RV rental. Or, get one delivered and set up for you.</p>
<div class="abs tabs">
  <span class="tab active"><i></i>Popular</span><span class="tab"><i></i>Camper van</span><span class="tab"><i></i>Value Deal</span><span class="tab"><i></i>Small trailer</span>
</div>

<article class="abs rental" style="left:131px;top:1700px">
  <div class="photo" style="background:linear-gradient(180deg,#a7b19a,#c9c3ad 55%,#6f6a56)" role="img" aria-label="Lightweight family travel trailer parked on grass"></div>
  <span class="abs deal">20% off</span><span class="abs fav"><svg width="11" height="10" viewBox="0 0 12 11" fill="none" stroke="#333" stroke-width="1.3"><path d="M6 10S1 6.5 1 3.5A2.5 2.5 0 0 1 6 2.5 2.5 2.5 0 0 1 11 3.5C11 6.5 6 10 6 10z"/></svg></span>
  <div class="abs dots"><i></i><i class="on"></i><i></i><i></i></div>
  <h3 class="abs">Lightweight Family Trailer</h3><div class="abs loc">&#9679; Filer, ID</div>
  <div class="abs tags"><span>Travel trailer</span><span>Sleeps 10</span><span>24 ft</span></div>
  <div class="abs price">$130 <small>/night</small></div><div class="abs rate"><i>&#9733;</i> 5.0(22)</div>
</article>
<article class="abs rental" style="left:451px;top:1700px">
  <div class="photo" style="background:linear-gradient(180deg,#6e95c2,#a9c1d8 55%,#b0a890)" role="img" aria-label="Toy hauler with off-road buggies on top under blue sky"></div>
  <span class="abs deal">20% off</span><span class="abs fav"><svg width="11" height="10" viewBox="0 0 12 11" fill="none" stroke="#333" stroke-width="1.3"><path d="M6 10S1 6.5 1 3.5A2.5 2.5 0 0 1 6 2.5 2.5 2.5 0 0 1 11 3.5C11 6.5 6 10 6 10z"/></svg></span>
  <div class="abs dots"><i></i><i class="on"></i><i></i><i></i></div>
  <h3 class="abs">Rv Dunerider toy hauler</h3><div class="abs loc">&#9679; Imperial, CA</div>
  <div class="abs tags"><span>Toy hauler</span><span>Sleeps 6</span><span>30 ft</span></div>
  <div class="abs price">$235 <small>/night</small></div><div class="abs rate"><i>&#9733;</i> 5.0(22)</div>
</article>
<article class="abs rental" style="left:769px;top:1700px">
  <div class="photo" style="background:linear-gradient(180deg,#d5dae0,#a4acb6 50%,#3c4048)" role="img" aria-label="Travel trailer with dark graphic stripes"></div>
  <span class="abs deal">Highly rated</span><span class="abs fav"><svg width="11" height="10" viewBox="0 0 12 11" fill="none" stroke="#333" stroke-width="1.3"><path d="M6 10S1 6.5 1 3.5A2.5 2.5 0 0 1 6 2.5 2.5 2.5 0 0 1 11 3.5C11 6.5 6 10 6 10z"/></svg></span>
  <div class="abs dots"><i></i><i class="on"></i><i></i><i></i></div>
  <h3 class="abs">Rv Dunerider toy hauler</h3><div class="abs loc">&#9679; Imperial, CA</div>
  <div class="abs tags"><span>Toy hauler</span><span>Sleeps 6</span><span>30 ft</span></div>
  <div class="abs price">$130 <small>/night</small></div><div class="abs rate"><i>&#9733;</i> 5.0(22)</div>
</article>

<article class="abs rental" style="left:131px;top:2075px">
  <div class="photo" style="background:linear-gradient(180deg,#c7cdd2,#8a949c 55%,#5d6469)" role="img" aria-label="Motorhome parked near a misty coastline"></div>
  <span class="abs deal">20% off</span><span class="abs fav"><svg width="11" height="10" viewBox="0 0 12 11" fill="none" stroke="#333" stroke-width="1.3"><path d="M6 10S1 6.5 1 3.5A2.5 2.5 0 0 1 6 2.5 2.5 2.5 0 0 1 11 3.5C11 6.5 6 10 6 10z"/></svg></span>
  <div class="abs dots"><i></i><i class="on"></i><i></i><i></i></div>
  <h3 class="abs">2007 Trailvane Explorer RS</h3><div class="abs loc">&#9679; Filer, ID</div>
  <div class="abs tags"><span>Travel trailer</span><span>Sleeps 10</span><span>24 ft</span></div>
  <div class="abs price">$245 <small>/night</small></div><div class="abs rate"><i>&#9733;</i> 5.0(22)</div>
</article>
<article class="abs rental" style="left:451px;top:2075px">
  <div class="photo" style="background:linear-gradient(180deg,#6e95c2,#a9c1d8 55%,#b0a890)" role="img" aria-label="Toy hauler with off-road buggies on top under blue sky"></div>
  <span class="abs deal">20% off</span><span class="abs fav"><svg width="11" height="10" viewBox="0 0 12 11" fill="none" stroke="#333" stroke-width="1.3"><path d="M6 10S1 6.5 1 3.5A2.5 2.5 0 0 1 6 2.5 2.5 2.5 0 0 1 11 3.5C11 6.5 6 10 6 10z"/></svg></span>
  <div class="abs dots"><i></i><i class="on"></i><i></i><i></i></div>
  <h3 class="abs">Rv Dunerider toy hauler</h3><div class="abs loc">&#9679; Imperial, CA</div>
  <div class="abs tags"><span>Toy hauler</span><span>Sleeps 6</span><span>30 ft</span></div>
  <div class="abs price">$235 <small>/night</small></div><div class="abs rate"><i>&#9733;</i> 5.0(22)</div>
</article>
<article class="abs rental" style="left:769px;top:2075px">
  <div class="photo" style="background:linear-gradient(180deg,#d5dae0,#a4acb6 50%,#3c4048)" role="img" aria-label="Travel trailer with dark graphic stripes"></div>
  <span class="abs deal">Highly rated</span><span class="abs fav"><svg width="11" height="10" viewBox="0 0 12 11" fill="none" stroke="#333" stroke-width="1.3"><path d="M6 10S1 6.5 1 3.5A2.5 2.5 0 0 1 6 2.5 2.5 2.5 0 0 1 11 3.5C11 6.5 6 10 6 10z"/></svg></span>
  <div class="abs dots"><i></i><i class="on"></i><i></i><i></i></div>
  <h3 class="abs">Rv Dunerider toy hauler</h3><div class="abs loc">&#9679; Imperial, CA</div>
  <div class="abs tags"><span>Toy hauler</span><span>Sleeps 6</span><span>30 ft</span></div>
  <div class="abs price">$130 <small>/night</small></div><div class="abs rate"><i>&#9733;</i> 5.0(22)</div>
</article>
<span class="abs btn" style="left:536px;top:2469px;width:128px;height:34px;font-size:12px">View all rentals</span>

<!-- Destinations -->
<h2 class="abs section-title" style="top:2548px">Popular RV Rental Destinations</h2>
<span class="abs arrow-btn" style="left:76px;top:2641px"><svg width="8" height="10" stroke="#555" stroke-width="1.5" fill="none"><path d="M6 1L2 5l4 4"/></svg></span>
<span class="abs arrow-btn" style="left:1098px;top:2641px"><svg width="8" height="10" stroke="#555" stroke-width="1.5" fill="none"><path d="M2 1l4 4-4 4"/></svg></span>
<div class="abs dest" style="left:93px"><svg width="22" height="28" viewBox="0 0 22 28" fill="none" stroke="#9a9d9f" stroke-width="1.6"><path d="M11 26s8-9 8-15a8 8 0 0 0-16 0c0 6 8 15 8 15z"/><circle cx="11" cy="11" r="3"/></svg><div><b>Atlanta, GA</b><span>751 RV rentals</span></div></div>
<div class="abs dest" style="left:300px"><svg width="22" height="28" viewBox="0 0 22 28" fill="none" stroke="#9a9d9f" stroke-width="1.6"><path d="M11 26s8-9 8-15a8 8 0 0 0-16 0c0 6 8 15 8 15z"/><circle cx="11" cy="11" r="3"/></svg><div><b>Austin, TX</b><span>783 RV rentals</span></div></div>
<div class="abs dest" style="left:506px"><svg width="22" height="28" viewBox="0 0 22 28" fill="none" stroke="#9a9d9f" stroke-width="1.6"><path d="M11 26s8-9 8-15a8 8 0 0 0-16 0c0 6 8 15 8 15z"/><circle cx="11" cy="11" r="3"/></svg><div><b>Boston, MA</b><span>351 RV rentals</span></div></div>
<div class="abs dest" style="left:713px"><svg width="22" height="28" viewBox="0 0 22 28" fill="none" stroke="#9a9d9f" stroke-width="1.6"><path d="M11 26s8-9 8-15a8 8 0 0 0-16 0c0 6 8 15 8 15z"/><circle cx="11" cy="11" r="3"/></svg><div><b>Chicago, IL</b><span>455 RV rentals</span></div></div>
<div class="abs dest" style="left:919px"><svg width="22" height="28" viewBox="0 0 22 28" fill="none" stroke="#9a9d9f" stroke-width="1.6"><path d="M11 26s8-9 8-15a8 8 0 0 0-16 0c0 6 8 15 8 15z"/><circle cx="11" cy="11" r="3"/></svg><div><b>Columbus, OH</b><span>410 RV rentals</span></div></div>

<!-- Feature -->
<div class="abs photo" style="left:63px;top:2736px;width:678px;height:501px;border-radius:16px 0 16px 16px;background:linear-gradient(180deg,#a8b49a 0%,#d9dde0 35%,#8e8c86 65%,#5c5650 100%)" role="img" aria-label="Owner handing RV keys to a smiling couple beside a motorhome"></div>
<aside class="abs feature-panel">
  <div class="feature-icon"></div>
  <p>Quellabyx connects local RV, motorhome and campervan owners with people and families wanting to rent them. Making memorable outdoor experiences accessible to everyone.</p>
  <p>Our RVs, travel trailers, and campervans have been driven over 160 million miles and booked over 2,000,000 travel days. Quellabyx is built on trust. We provide the highest level of safety so you can focus on making memories of a lifetime. When you book with us, you rent worry-free because we offer:</p>
  <div class="perk"><svg width="14" height="14" fill="none" stroke="#777" stroke-width="1.3"><path d="M7 12S1 8 1 4.5a3 3 0 0 1 6-1 3 3 0 0 1 6 1C13 8 7 12 7 12z"/></svg><div><b>We truly care</b><span>From our team to our community of owners, we are all about the things that make you feel welcome wherever you go</span></div></div>
  <div class="perk"><svg width="14" height="14" fill="none" stroke="#777" stroke-width="1.3"><rect x="1" y="4" width="12" height="7" rx="1"/><circle cx="4" cy="12" r="1.2"/><circle cx="10" cy="12" r="1.2"/></svg><div><b>24/7 Roadside Assistance</b><span>Worry-free roadside assistance when you need it</span></div></div>
  <div class="perk"><svg width="14" height="14" fill="none" stroke="#777" stroke-width="1.3"><path d="M7 1l5 2v4c0 3-2.5 5-5 6-2.5-1-5-3-5-6V3z"/><path d="M4.5 7l2 2 3-3"/></svg><div><b>Insurance protection</b><span>$1M insurance protection covering the renter, owner, and vehicle</span></div></div>
  <div class="perk"><svg width="14" height="14" fill="none" stroke="#777" stroke-width="1.3"><circle cx="7" cy="7" r="6"/><path d="M4 7h6M7 4v6"/></svg><div><b>24/7 Support</b><span>Real people here to help. 24/7 customer support via email, phone, and on-site chat.</span></div></div>
</aside>

<!-- Parks -->
<div class="abs parks-bg"></div>
<h2 class="abs head-font" style="left:63px;top:3318px;font-size:29px;font-weight:700">Explore rentals near National Parks</h2>
<p class="abs" style="left:63px;top:3360px;font-size:14px;color:var(--muted)">Cruise to epic locations in the comfort of an RV rental. From <b style="color:var(--ink)">$45/night</b></p>
<span class="abs arrow-btn" style="left:1068px;top:3357px;opacity:.45"><svg width="8" height="10" stroke="#555" stroke-width="1.5" fill="none"><path d="M6 1L2 5l4 4"/></svg></span>
<span class="abs arrow-btn" style="left:1108px;top:3357px"><svg width="8" height="10" stroke="#333" stroke-width="1.5" fill="none"><path d="M2 1l4 4-4 4"/></svg></span>
<article class="abs park photo" style="left:63px;background:linear-gradient(180deg,#4e7fb4 0%,#a9c3dc 40%,#c9d2d8 60%,#6a6a5a 100%)" role="img" aria-label="Geyser erupting in Yellowstone">
  <span class="abs fav"><svg width="14" height="13" viewBox="0 0 12 11" fill="none" stroke="#333" stroke-width="1.2"><path d="M6 10S1 6.5 1 3.5A2.5 2.5 0 0 1 6 2.5 2.5 2.5 0 0 1 11 3.5C11 6.5 6 10 6 10z"/></svg></span>
  <h3 class="abs">Yellowstone</h3><span class="abs region">Wyoming</span><span class="abs book">Book Now</span>
  <div class="abs dots"><i></i><i class="on"></i><i></i></div></article>
<article class="abs park photo" style="left:428px;background:linear-gradient(180deg,#7f8eb0 0%,#b76a4a 40%,#8b4a34 65%,#3f5a3a 100%)" role="img" aria-label="Red rock canyon and river in Zion">
  <span class="abs fav"><svg width="14" height="13" viewBox="0 0 12 11" fill="none" stroke="#333" stroke-width="1.2"><path d="M6 10S1 6.5 1 3.5A2.5 2.5 0 0 1 6 2.5 2.5 2.5 0 0 1 11 3.5C11 6.5 6 10 6 10z"/></svg></span>
  <h3 class="abs">Zion</h3><span class="abs region">Utah</span><span class="abs book">Book Now</span>
  <div class="abs dots"><i></i><i class="on"></i><i></i></div></article>
<article class="abs park photo" style="left:794px;background:linear-gradient(180deg,#9fb0bd 0%,#5e6f66 40%,#34462f 70%,#24331f 100%)" role="img" aria-label="Forested mountains in Glacier">
  <span class="abs fav"><svg width="14" height="13" viewBox="0 0 12 11" fill="none" stroke="#333" stroke-width="1.2"><path d="M6 10S1 6.5 1 3.5A2.5 2.5 0 0 1 6 2.5 2.5 2.5 0 0 1 11 3.5C11 6.5 6 10 6 10z"/></svg></span>
  <h3 class="abs">Glacier</h3><span class="abs region">Montana</span><span class="abs book">Book Now</span>
  <div class="abs dots"><i></i><i class="on"></i><i></i></div></article>

<!-- News -->
<h2 class="abs section-title" style="top:3906px">Latest news</h2>
<article class="abs news" style="left:63px">
  <div class="photo" style="background:linear-gradient(160deg,#d9602c,#b3452a 45%,#3b4a3c)" role="img" aria-label="Feet resting in a hammock beside an orange camper van"></div>
  <span class="abs tag">+ LATEST</span>
  <h3 class="abs">The Quellabyx Group Exceeds $3 Billion in Sales, Plans European Expansion</h3>
  <p class="abs excerpt">"The Quellabyx Group has leveraged its strategic advantages to thrive even amidst the economic challenges that have impacted consumers and leisure travel over the past 12 months," said the team.</p>
  <span class="abs more">Read More</span></article>
<article class="abs news" style="left:428px">
  <div class="photo" style="background:linear-gradient(180deg,#d9cdb8,#b99a74 50%,#6a5a48)" role="img" aria-label="Friends relaxing in camp chairs beside an RV"></div>
  <span class="abs tag">+ Jan 25</span>
  <h3 class="abs">The Quellabyx Group Exceeds $3 Billion in Sales, Plans European Expansion</h3>
  <p class="abs excerpt">"The Quellabyx Group has leveraged its strategic advantages to thrive even amidst the economic challenges that have impacted consumers and leisure travel over the past 12 months," said the team.</p>
  <span class="abs more">Read More</span></article>
<article class="abs news" style="left:794px">
  <div class="photo" style="background:linear-gradient(180deg,#8fb4d8,#c9dbe6 40%,#5f7d3e 75%,#44612b)" role="img" aria-label="White camper van parked in a green pine forest"></div>
  <span class="abs tag">+ Jan 25</span>
  <h3 class="abs">The Quellabyx Group Exceeds $3 Billion in Sales, Plans European Expansion</h3>
  <p class="abs excerpt">"The Quellabyx Group has leveraged its strategic advantages to thrive even amidst the economic challenges that have impacted consumers and leisure travel over the past 12 months," said the team.</p>
  <span class="abs more">Read More</span></article>
<span class="abs btn" style="left:536px;top:4437px;width:128px;height:34px;font-size:12px">View all News</span>

<!-- Footer -->
<footer class="abs site-footer">
  <div class="abs footer-brand">Zandoprik.com</div>
  <div class="abs socials"><i></i><i></i><i></i><i></i><i></i></div>
  <div class="abs footer-col" style="left:380px"><h4>About Us</h4><ul><li>Where it all began</li><li>Careers</li><li>Stories and news</li><li>Travel journal</li><li>About</li></ul></div>
  <div class="abs footer-col" style="left:561px"><h4>Guest travel</h4><ul><li>Group bookings</li><li>Gift cards</li><li>Delivery</li><li>National park guides</li><li>One-way rentals</li><li>Road trip guides</li><li>RV parks &amp; campgrounds</li><li>Guide to all RV types</li></ul></div>
  <div class="abs footer-col" style="left:768px"><h4>Hosting</h4><ul><li>Become an RV host</li><li>Hostdeck demo</li><li>Affiliate program</li><li>RV insurance</li></ul></div>
  <div class="abs footer-col" style="left:968px"><h4>Support</h4><ul><li>How it works</li><li>Help center</li><li>Contact us</li><li>Give us feedback</li></ul></div>
</footer>
<div class="abs legal"><span>© 2026 Zandoprik.com. All rights reserved.</span><span>Terms | Privacy | Sitemap</span></div>

</body>
</html>
```